Monthly Planner & To Do List on dry erase magnetic whiteboard

I'm after 2 x designs for magnetic whiteboards.
1. 17 x 13 inches is a monthly planner. Dates and month can be written in each month and then wiped off and re-written for the next month.
2. 6 x 4 inches - to do list however I don't want this to say To Do on it but will have lines to write on and possibly bullet points to check off.
I have attached below samples of other products (the ones I like the most are the first two - 9.19.52 and 9.20.34). I actually don't like the design of the others but just show them here as an example for layout purposes.
I want something that is modern, slick, simple yet stylish which is what my brand is representative of - smart, modern, organised. It will be printed onto a white board and I only want the print to be in black, no grey shading. I need a more modern font and don't like any of the swirly parts. Just clean and simple but slick.
I would like the size of the day squares to be as large as possible to fit writing in them and also for a section somewhere on the page for additional notes.

Requirements
Should not have
• Old style fonts, cartoon style or childish.

```html
<!DOCTYPE html>
<html lang="en">
<head>
<meta charset="utf-8">
<title>Monthly Planner</title>
<link rel="stylesheet" href="https://fonts.googleapis.com/css2?family=Roboto+Condensed:wght@700&family=Roboto:wght@300;400;700&display=swap">
<style>
  :root {
    --ink: #000000;
    --paper: #ffffff;
  }
  html, body {
    margin: 0;
    padding: 0;
    overflow: hidden;
    background: var(--paper);
  }
  .planner {
    position: relative;
    width: 1200px;
    height: 918px;
    overflow: hidden;
    background: var(--paper);
    font-family: "Roboto", Arial, sans-serif;
    color: var(--ink);
  }
  .month-field {
    position: absolute;
    left: 46px;
    top: 96px;
    width: 330px;
    height: 0;
    border-top: 2px solid var(--ink);
  }
  .year-block {
    position: absolute;
    right: 35px;
    top: 26px;
    width: 150px;
    text-align: right;
    line-height: 1;
  }
  .year-field {
    display: block;
    height: 44px;
    border-bottom: 2px solid var(--ink);
  }
  .label {
    display: block;
    margin-top: 6px;
    font-weight: 300;
    font-size: 29px;
    letter-spacing: 0.5px;
  }
  .calendar {
    position: absolute;
    left: 46px;
    top: 114px;
    width: 1119px;
    display: grid;
    grid-template-columns: repeat(7, 157px);
    column-gap: 3.3px;
  }
  .weekday {
    height: 34px;
    background: var(--ink);
    color: var(--paper);
    font-size: 16px;
    line-height: 34px;
    padding-left: 11px;
  }
  .weeks {
    grid-column: 1 / -1;
    display: grid;
    grid-template-columns: repeat(7, 157px);
    grid-auto-rows: 106px;
    column-gap: 3.3px;
    row-gap: 5.5px;
    margin-top: 4px;
  }
  .day {
    box-sizing: border-box;
    border: 1.3px solid var(--ink);
  }
  .notes {
    position: absolute;
    left: 48px;
    top: 749px;
    width: 820px;
    margin: 0;
    padding: 0;
    list-style: none;
  }
  .notes li {
    height: 0;
    border-top: 1px solid var(--ink);
    margin-bottom: 30px;
  }
  .task-card {
    position: absolute;
    left: 900px;
    top: 722px;
    width: 265px;
    height: 176px;
    box-sizing: border-box;
    border: 1.3px solid var(--ink);
    padding: 14px 18px;
    margin: 0;
    list-style: none;
  }
  .task {
    display: flex;
    align-items: flex-end;
    gap: 10px;
    height: 29px;
  }
  .task-box {
    flex: none;
    width: 12px;
    height: 12px;
    box-sizing: border-box;
    border: 1.3px solid var(--ink);
    margin-bottom: 3px;
  }
  .task-line {
    flex: 1;
    height: 0;
    border-top: 1px solid var(--ink);
  }
</style>
</head>
<body>
<main class="planner">
  <div class="month-field" aria-label="Write month here"></div>
  <div class="year-block">
    <span class="year-field" aria-label="Write year here"></span>
    <span class="label">PLANNER</span>
  </div>

  <section class="calendar">
    <div class="weekday">SUN</div>
    <div class="weekday">MON</div>
    <div class="weekday">TUE</div>
    <div class="weekday">WED</div>
    <div class="weekday">THR</div>
    <div class="weekday">FRI</div>
    <div class="weekday">SAT</div>

    <div class="weeks">
      <div class="day"></div><div class="day"></div><div class="day"></div><div class="day"></div><div class="day"></div><div class="day"></div><div class="day"></div>
      <div class="day"></div><div class="day"></div><div class="day"></div><div class="day"></div><div class="day"></div><div class="day"></div><div class="day"></div>
      <div class="day"></div><div class="day"></div><div class="day"></div><div class="day"></div><div class="day"></div><div class="day"></div><div class="day"></div>
      <div class="day"></div><div class="day"></div><div class="day"></div><div class="day"></div><div class="day"></div><div class="day"></div><div class="day"></div>
      <div class="day"></div><div class="day"></div><div class="day"></div><div class="day"></div><div class="day"></div><div class="day"></div><div class="day"></div>
    </div>
  </section>

  <ul class="notes" aria-label="Notes">
    <li></li>
    <li></li>
    <li></li>
    <li></li>
    <li></li>
  </ul>

  <ul class="task-card" aria-label="Task list">
    <li class="task"><span class="task-box"></span><span class="task-line"></span></li>
    <li class="task"><span class="task-box"></span><span class="task-line"></span></li>
    <li class="task"><span class="task-box"></span><span class="task-line"></span></li>
    <li class="task"><span class="task-box"></span><span class="task-line"></span></li>
    <li class="task"><span class="task-box"></span><span class="task-line"></span></li>
  </ul>
</main>
</body>
</html>
```